Political Mail Out Quintero front and back

Front
Esteban (9th Grade) Quintero!

What's that famous saying?

Show me who your friends are and I'll tell you who you really are!
(show the two guys)

Walter Cuellar is charged with voter fraud by changing voter addresses from across the RGV so they could vote in Edinburg
Back
Did Esteban (9th Grade) Quintero commit voter fraud when he ran for office in 2016?
(insert blurred photo)

Here is a list of people from all over the RGV that voted in Edinburg in the 2016 race.
Here is a break down:

(highlight the number and where they were first registered to vote)

9 People voted in Edinburg who were registered in Donna.
13 People voted in Edinburg who were registered in San Juan
8 People voted in Edinburg who were registered in Pharr
31 People voted in Edinburg who were registered in McAllen
2 People voted in Edinburg who were registered in La Joya
6 People voted in Edinburg who were registered in Edcouch
2 People voted in Edinburg who were registered in Mercedes
2 People voted in Edinburg who were registered in Monte Alto
6 People voted in Edinburg who were registered in Weslaco
1 Person voted in Edinburg who were registered in Penitas
3 People voted in Edinburg who were registered in Alamo
5 People voted in Edinburg who were registered in Elsa
6 People voted in Edinburg who were registered in Mission
1 Person voted in Edinburg who were registered in Alton

Will Esteban (9th Grade) Quintero CHEAT in 2020?

Only time will tell.

Vote Esteban (9th Grade) Quintero OUT of office.

```html
<!DOCTYPE html>
<html lang="en">
<head>
<meta charset="utf-8">
<title>Quintero Mail Out – Front and Back</title>
<link rel="stylesheet" href="https://fonts.googleapis.com/css2?family=Bebas+Neue&family=Roboto:wght@400;700&display=swap">
<style>
  :root {
    --backdrop: #3b3b3d;
    --paper: #ffffff;
    --paper-shade: #eeeeee;
    --red: #e31e24;
    --ink: #1a1a1a;
    --slate: #4a4a4a;
    --photo-warm: #8a5a3c;
    --photo-dark: #3a2a20;
    --screen-grey: #b8b8b8;
  }
  * { margin: 0; padding: 0; box-sizing: border-box; }
  html, body { width: 1200px; height: 806px; overflow: hidden; background: var(--backdrop); }
  .canvas { position: relative; width: 1200px; height: 806px; }

  .page {
    position: absolute; top: 62px; width: 527px; height: 682px;
    background: linear-gradient(135deg, var(--paper) 0%, var(--paper-shade) 55%, var(--paper) 100%);
    font-family: "Bebas Neue", "Oswald", sans-serif;
  }
  .page--front { left: 62px; }
  .page--back { left: 611px; }

  /* Front */
  .headline {
    position: absolute; top: 56px; left: 0; width: 100%;
    display: flex; justify-content: center; align-items: center; gap: 8px;
    color: var(--red); font-size: 66px; line-height: 1; white-space: nowrap;
  }
  .headline__grade { color: var(--ink); font-size: 29px; line-height: 0.85; text-align: center; }
  .saying-frame {
    position: absolute; left: 22px; top: 175px; width: 482px; height: 323px;
    border: 3px solid var(--ink);
  }
  .saying-frame__label {
    position: absolute; top: -14px; left: 50%; transform: translateX(-50%);
    background: var(--paper); padding: 0 18px; color: var(--red); font-size: 26px; line-height: 1; white-space: nowrap;
  }
  .saying-frame__quote {
    position: absolute; top: 22px; left: 0; width: 100%;
    text-align: center; color: var(--slate); font-size: 36px; line-height: 1.05;
  }
  .friends-photo {
    position: absolute; left: 52px; top: 297px; width: 422px; height: 254px;
    border: 4px solid var(--red);
    background: linear-gradient(120deg, var(--photo-dark) 0%, var(--photo-warm) 50%, var(--photo-dark) 100%);
  }
  .charge-note {
    position: absolute; top: 590px; left: 0; width: 100%;
    text-align: center; color: var(--red); font-size: 20px; line-height: 1.25;
  }

  /* Back */
  .question-box {
    position: absolute; left: 48px; top: 54px; width: 250px; height: 156px;
    border: 4px solid #333; background: var(--paper);
    padding: 20px 0 0 18px; color: var(--slate); font-size: 24px; line-height: 1.05;
  }
  .records-photo {
    position: absolute; left: 283px; top: 35px; width: 212px; height: 195px;
    border: 4px solid var(--red);
    background: linear-gradient(90deg, var(--screen-grey) 0%, #d8d8d8 30%, #c4c4c4 100%);
  }
  .list-intro {
    position: absolute; top: 254px; left: 0; width: 100%;
    text-align: center; color: var(--red); font-size: 19px; line-height: 1.38;
  }
  .tally {
    position: absolute; top: 307px; left: 54px; width: 440px;
    font-family: "Roboto", Arial, sans-serif; font-size: 12.6px; color: var(--ink); line-height: 15.9px;
  }
  .tally__row { text-align: justify; text-align-last: justify; }
  .tally__row b { font-weight: 700; }
  .cheat-question {
    position: absolute; top: 541px; left: 0; width: 100%;
    text-align: center; color: var(--red); font-size: 23px; line-height: 1;
  }
  .verdict-frame {
    position: absolute; left: 18px; top: 584px; width: 489px; height: 59px;
    border: 3px solid var(--red);
  }
  .verdict-frame__label {
    position: absolute; top: -16px; left: 50%; transform: translateX(-50%);
    background: var(--paper); padding: 0 14px; color: var(--red); font-size: 27px; line-height: 1; white-space: nowrap;
  }
  .verdict-frame__call {
    position: absolute; top: 22px; left: 0; width: 100%;
    text-align: center; color: var(--slate); font-size: 26px; line-height: 1; white-space: nowrap;
  }
</style>
</head>
<body>
<div class="canvas">

  <section class="page page--front">
    <h1 class="headline">
      <span>Esteban</span>
      <span class="headline__grade">9th<br>Grade</span>
      <span>Quintero!</span>
    </h1>
    <div class="saying-frame">
      <h2 class="saying-frame__label">What's that famous saying?</h2>
      <p class="saying-frame__quote">Show me who your friends are and<br>I'll tell you who you really are!</p>
    </div>
    <div class="friends-photo" role="img" aria-label="Photo of two smiling men posing together, one in a campaign polo shirt"></div>
    <p class="charge-note">Walter Cuellar is charged with voter fraud by changing voter<br>addresses from across the RGV so they could vote in Edinburg</p>
  </section>

  <section class="page page--back">
    <h2 class="question-box">Did Esteban (9th Grade)<br>Quintero commit voter<br>fraud when he ran<br>for office in 2016?</h2>
    <div class="records-photo" role="img" aria-label="Blurred photo of a voter address record listing on screen"></div>
    <p class="list-intro">Here is a list of people from all over the RGV that voted in<br>Edinburg in the 2016 race. Here is a break down:</p>
    <div class="tally">
      <p class="tally__row"><b>9 People</b> voted in Edinburg who were registered in <b>Donna.</b></p>
      <p class="tally__row"><b>13 People</b> voted in Edinburg who were registered in <b>San Juan</b></p>
      <p class="tally__row"><b>8 People</b> voted in Edinburg who were registered in <b>Pharr</b></p>
      <p class="tally__row"><b>31 People</b> voted in Edinburg who were registered in <b>McAllen</b></p>
      <p class="tally__row"><b>2 People</b> voted in Edinburg who were registered in <b>La Joya</b></p>
      <p class="tally__row"><b>6 People</b> voted in Edinburg who were registered in <b>Edcouch</b></p>
      <p class="tally__row"><b>2 People</b> voted in Edinburg who were registered in <b>Mercedes</b></p>
      <p class="tally__row"><b>2 People</b> voted in Edinburg who were registered in <b>Monte Alto</b></p>
      <p class="tally__row"><b>6 People</b> voted in Edinburg who were registered in <b>Weslaco</b></p>
      <p class="tally__row"><b>1 Person</b> voted in Edinburg who were registered in <b>Penitas</b></p>
      <p class="tally__row"><b>3 People</b> voted in Edinburg who were registered in <b>Alamo</b></p>
      <p class="tally__row"><b>5 People</b> voted in Edinburg who were registered in <b>Elsa</b></p>
      <p class="tally__row"><b>6 People</b> voted in Edinburg who were registered in <b>Mission</b></p>
      <p class="tally__row"><b>1 Person</b> voted in Edinburg who were registered in <b>Alton</b></p>
    </div>
    <p class="cheat-question">Will Esteban (9th Grade) Quintero cheat in 2020?</p>
    <div class="verdict-frame">
      <p class="verdict-frame__label">Only time will tell.</p>
      <p class="verdict-frame__call">Vote Esteban (9th Grade) Quintero out of office.</p>
    </div>
  </section>

</div>
</body>
</html>
```